Redesign Business Cards, Attached

Please read instructions carefully. If you have any questions send a message before submitting your ONE design. Please redesign attached business cards. Double sided. Use same content and descriptions. Use black, silver, crimson red and gold colors. My only issue with the attached design is the background colors. I like the layout as-is. I can provide the individual pictures on the back side later. Do not submit more than one design. One submission shall include both front and back. Do not submit front and back separately. A second project will be launched to create a matching post card after completion of this.
Industry/Entity Type
see description and attachments.
Contact Information for Business Card
Requirements
Must have
- see description and attachments.
Nice to have
Should not have

```html
<!DOCTYPE html>
<html lang="en">
<head>
<meta charset="utf-8">
<title>Helmsway Business Card – Front and Back</title>
<link href="https://fonts.googleapis.com/css2?family=Montserrat:wght@400;500;600;700;800&display=swap" rel="stylesheet">
<style>
  :root {
    --black: #141414;
    --black-deep: #050505;
    --crimson: #a3122a;
    --gold: #e2b64a;
    --silver: #c9ccd1;
    --silver-light: #e6e8eb;
    --white: #ffffff;
    --backdrop: #d6d6d2;
    --sea-light: #dbe9f5;
    --sea-mid: #8fb3d6;
    --sea-dark: #3f6e9c;
  }
  * { margin: 0; padding: 0; box-sizing: border-box; }
  html, body { width: 1200px; height: 801px; overflow: hidden; }
  body {
    background: var(--backdrop);
    font-family: "Montserrat", sans-serif;
    position: relative;
  }
  .card {
    position: absolute;
    top: 240px;
    width: 560px;
    height: 320px;
    overflow: hidden;
    box-shadow: 0 12px 30px rgba(0,0,0,0.25);
  }
  .card-front { left: 26px; background: var(--black); }
  .card-back { left: 614px; background: var(--white); }
  .card-art { position: absolute; inset: 0; }

  /* Front */
  .brand {
    position: absolute;
    left: 24px; top: 172px;
    width: 92px; height: 92px;
    border-radius: 50%;
    background: var(--silver-light);
    border: 3px solid var(--gold);
    display: flex; align-items: center; justify-content: center;
  }
  .brand-name {
    font-weight: 700;
    font-size: 13px;
    letter-spacing: 1px;
    color: var(--black);
  }
  .identity {
    position: absolute;
    left: 134px; top: 170px;
    color: var(--silver-light);
  }
  .person-name {
    font-weight: 700;
    font-size: 21px;
    letter-spacing: 1px;
    color: var(--gold);
    text-transform: uppercase;
  }
  .person-role {
    font-weight: 400;
    font-size: 14px;
    line-height: 1.3;
    margin-top: 2px;
  }
  .contacts { list-style: none; margin-top: 10px; }
  .contact {
    display: flex; align-items: center; gap: 8px;
    font-weight: 600; font-size: 13px; line-height: 20px;
  }
  .contact svg { width: 13px; height: 13px; flex: none; }

  /* Back */
  .badge {
    position: absolute;
    top: 28px;
    width: 74px; height: 74px;
    border-radius: 14px;
    background: var(--white);
    display: flex; align-items: center; justify-content: center;
  }
  .badge-one { left: 150px; }
  .badge-two { left: 236px; }
  .badge-mark {
    width: 48px; height: 48px; border-radius: 50%;
    background: var(--silver-light);
    border: 3px solid var(--silver);
  }
  .services {
    position: absolute;
    left: 36px; top: 146px;
    display: grid;
    grid-template-columns: repeat(4, 118px);
    grid-template-rows: repeat(2, 54px);
    gap: 6px;
  }
  .service {
    display: flex; align-items: center; justify-content: center;
    text-align: center;
    font-weight: 600; font-size: 11px; line-height: 1.25;
    padding: 0 6px;
  }
  .service-crimson { background: var(--crimson); color: var(--white); }
  .service-gold { background: var(--gold); color: var(--black); }
  .site {
    position: absolute;
    left: 0; right: 0; bottom: 24px;
    text-align: center;
    font-weight: 700; font-size: 16px;
    letter-spacing: 3px;
    color: var(--black);
  }
</style>
</head>
<body>

<section class="card card-front" aria-label="Business card front">
  <svg class="card-art" viewBox="0 0 560 320">
    <defs>
      <linearGradient id="seaFront" x1="0" y1="0" x2="1" y2="1">
        <stop offset="0" stop-color="var(--sea-light)"/>
        <stop offset="0.6" stop-color="var(--sea-mid)"/>
        <stop offset="1" stop-color="var(--sea-dark)"/>
      </linearGradient>
    </defs>
    <circle cx="460" cy="-30" r="182" fill="var(--black-deep)"/>
    <circle cx="460" cy="-30" r="174" fill="url(#seaFront)" role="img" aria-label="Photo of a white centre-console boat speeding over sparkling water"/>
    <path d="M275,3 A188 188 0 0 0 509,152" fill="none" stroke="var(--gold)" stroke-width="10" stroke-linecap="round"/>
  </svg>

  <div class="brand"><span class="brand-name">HELMSWAY</span></div>

  <div class="identity">
    <h1 class="person-name">Jordan T. Halvers</h1>
    <p class="person-role">USCG Licensed Captain<br>Certified Instructor</p>
    <ul class="contacts">
      <li class="contact">
        <svg viewBox="0 0 24 24"><path fill="var(--gold)" d="M6.6 10.8a15 15 0 0 0 6.6 6.6l2.2-2.2a1 1 0 0 1 1-.25 11.4 11.4 0 0 0 3.6.57 1 1 0 0 1 1 1V20a1 1 0 0 1-1 1A17 17 0 0 1 3 4a1 1 0 0 1 1-1h3.5a1 1 0 0 1 1 1c0 1.25.2 2.45.57 3.57a1 1 0 0 1-.25 1z"/></svg>
        (555) 014-2290
      </li>
      <li class="contact">
        <svg viewBox="0 0 24 24"><rect x="2" y="5" width="20" height="14" rx="1" fill="none" stroke="var(--gold)" stroke-width="2"/><path d="M2 6l10 7 10-7" fill="none" stroke="var(--gold)" stroke-width="2"/></svg>
        service@helmcoach.com
      </li>
      <li class="contact">
        <svg viewBox="0 0 24 24"><circle cx="12" cy="12" r="10" fill="none" stroke="var(--gold)" stroke-width="2"/><ellipse cx="12" cy="12" rx="4" ry="10" fill="none" stroke="var(--gold)" stroke-width="2"/><path d="M2 12h20" stroke="var(--gold)" stroke-width="2"/></svg>
        www.helmcoach.com
      </li>
    </ul>
  </div>
</section>

<section class="card card-back" aria-label="Business card back">
  <svg class="card-art" viewBox="0 0 560 320">
    <defs>
      <linearGradient id="seaBack" x1="0" y1="0" x2="1" y2="1">
        <stop offset="0" stop-color="var(--sea-light)"/>
        <stop offset="0.5" stop-color="var(--sea-mid)"/>
        <stop offset="1" stop-color="var(--sea-dark)"/>
      </linearGradient>
    </defs>
    <polygon points="0,0 560,0 560,168 0,250" fill="var(--black)"/>
    <polygon points="318,0 560,0 560,132 372,150 300,70" fill="var(--silver)"/>
    <polygon points="326,0 560,0 560,124 376,142 310,70" fill="url(#seaBack)" role="img" aria-label="Photo of a white boat cruising across open blue water"/>
  </svg>

  <div class="badge badge-one" role="img" aria-label="Membership badge"><span class="badge-mark"></span></div>
  <div class="badge badge-two" role="img" aria-label="Instructor certification badge"><span class="badge-mark"></span></div>

  <div class="services">
    <div class="service service-crimson">Hands-on Boat Training</div>
    <div class="service service-gold">Introduction to Power boating</div>
    <div class="service service-crimson">Precision Docking &amp; Boat Handling</div>
    <div class="service service-gold">Open Water Boat Handling</div>
    <div class="service service-gold">Island Anchoring</div>
    <div class="service service-crimson">Open Water Advanced Maneuvers</div>
    <div class="service service-gold">Coastal Navigation</div>
    <div class="service service-crimson">Captaining / piloting Service for Your Outings</div>
  </div>

  <p class="site">www.helmcoach.com</p>
</section>

</body>
</html>
```